Rent Kiosks and Tablets

Website for rental kiosks and tablets following the model / style http://www.quellstander.com/. May be the same, with changes in visual identity.
The site should also have an online order system like an e-commerce, which allows payment by credit card and ticket.

The company is called Bolumexa.com and feel free to create/suggest styles of names design.

Target Market(s)

Events, trade shows, marketing companies.

Industry/Entity Type

Credit Card

Font styles to use
Sans Serif

Colors

Designer to choose colors to be used in the design.

```html
<!DOCTYPE html>
<html lang="en">
<head>
<meta charset="utf-8">
<title>Bolumexa — Rent Kiosks and Tablets</title>
<link href="https://fonts.googleapis.com/css2?family=Open+Sans:wght@400;600;700&display=swap" rel="stylesheet">
<style>
:root{
  --yellow:#f6b911;
  --yellow-dark:#e0a400;
  --orange:#e4951b;
  --ink:#333;
  --muted:#8a8a8a;
  --line:#e3e3e3;
  --footer-light:#ececec;
  --footer-dark:#2e2e2e;
  --chip:#9a9a9a;
}
*{box-sizing:border-box;margin:0;padding:0}
html,body{width:779px;height:1200px;overflow:hidden;background:#fff}
body{font-family:"Open Sans",Arial,sans-serif;color:var(--ink);position:relative}
.topline{height:4px;background:var(--yellow)}
.wrap{width:650px;margin:0 auto;position:relative}
.header{height:66px;display:flex;align-items:center;justify-content:space-between}
.brand{font-size:34px;font-weight:400;color:#444;letter-spacing:-0.5px}
.callus{font-size:13px;color:#666;display:flex;align-items:center;gap:6px}
.callus b{color:var(--ink);font-weight:600}
.nav{height:26px;background:var(--yellow);display:flex;align-items:center;padding:0 8px}
.nav a{font-size:9px;font-weight:600;color:#3a2d00;text-decoration:none;padding:0 12px;height:26px;line-height:26px}
.nav a.active{background:#fff}
.search{margin-left:auto;width:140px;height:16px;background:#fff;border:1px solid #d9a000;font-size:8px;color:#999;padding:0 5px;line-height:14px;position:relative}
.search svg{position:absolute;right:4px;top:3px}
.hero{height:314px;position:relative;background:linear-gradient(135deg,#d9d6cf 0%,#b7b1a6 35%,#8b8275 60%,#cfcac1 100%)}
.hero-arrow{position:absolute;top:147px;width:22px;height:22px;border-radius:50%;background:rgba(255,255,255,.8);display:flex;align-items:center;justify-content:center}
.hero-arrow.left{left:10px}.hero-arrow.right{right:10px}
.hero-caption{position:absolute;right:40px;top:205px;width:200px;background:rgba(255,255,255,.85);padding:10px 12px;text-align:right}
.hero-caption p{font-size:14px;line-height:1.35;color:#333}
.btn{display:inline-block;margin-top:8px;background:var(--yellow);color:#3a2d00;font-size:11px;font-weight:600;padding:5px 10px}
.hero-rule{height:5px;background:var(--yellow);margin-top:6px}
.features{display:flex;justify-content:space-between;margin-top:16px}
.feature{width:204px}
.feature .thumb{height:114px}
.feature h3{font-size:11px;font-weight:400;margin-top:10px;color:#555}
.feature h3 span{font-size:15px;color:#222}
.thumb.kiosks{background:linear-gradient(135deg,#6fa7b0,#1f6f7a 50%,#c8ccd0)}
.thumb.tablets{background:linear-gradient(135deg,#f2f2f2,#c9c9c9 55%,#9a9a9a)}
.thumb.about{background:linear-gradient(135deg,#2b2b2b,#4b4b4b);display:flex;align-items:center;justify-content:center}
.divider{height:1px;background:var(--line)}
.intro{display:flex;margin-top:14px;gap:20px;height:200px}
.intro-text{width:480px;padding-top:18px}
.intro h2{font-size:15px;font-weight:400;color:var(--orange);margin-bottom:10px}
.intro p{font-size:8px;line-height:1.55;color:#777;margin-bottom:10px}
.intro-photo{width:150px;height:196px;background:linear-gradient(180deg,#f4f1ee,#d8d2cc 60%,#f1eeea)}
.platforms{display:flex;justify-content:space-around;align-items:center;height:70px;margin-top:22px;padding:0 10px}
.platform{font-size:26px;font-weight:400;color:#444}
.tagline{text-align:center;font-size:11px;line-height:1.6;color:#888;margin:22px 40px 0}
.partners{display:flex;justify-content:space-between;margin-top:38px;padding:0 6px}
.partners span{display:block;width:52px;height:14px;background:#cfcfcf;border-radius:2px}
.footer-info{position:absolute;left:0;right:0;top:1080px;height:60px;background:var(--footer-light)}
.footer-info .wrap{display:flex;justify-content:space-between;align-items:center;height:60px;font-size:8px;color:#777}
.footer-info .item{display:flex;align-items:center;gap:6px}
.footer-bar{position:absolute;left:0;right:0;top:1140px;height:60px;background:var(--footer-dark)}
.footer-bar .wrap{padding-top:10px}
.footer-links a{font-size:8px;color:#ccc;text-decoration:none;margin-right:4px}
.footer-bar p{font-size:8px;color:#aaa;margin-top:8px}
.social{position:absolute;right:0;top:10px;display:flex;gap:4px}
.social i{display:block;width:14px;height:14px;background:var(--chip);border-radius:2px}
</style>
</head>
<body>
<div class="topline"></div>
<div class="wrap">
  <header class="header">
    <div class="brand">bolumexa</div>
    <div class="callus">
      <svg width="14" height="14" viewBox="0 0 24 24"><path fill="#555" d="M6.6 10.8a15 15 0 0 0 6.6 6.6l2.2-2.2c.3-.3.7-.4 1-.2 1.1.4 2.3.6 3.6.6.6 0 1 .4 1 1V20c0 .6-.4 1-1 1A17 17 0 0 1 3 4c0-.6.4-1 1-1h3.5c.6 0 1 .4 1 1 0 1.3.2 2.5.6 3.6.1.3 0 .7-.2 1z"/></svg>
      Call us : <b>555 014 2290</b>
    </div>
  </header>
  <nav class="nav">
    <a class="active">HOME</a><a>ABOUT</a><a>SERVICES</a><a>PRODUCTS</a><a>PRICING</a><a>CONTACT</a>
    <div class="search">Search
      <svg width="9" height="9" viewBox="0 0 10 10"><circle cx="4" cy="4" r="3" fill="none" stroke="#888" stroke-width="1.3"/><path d="M6.3 6.3 9 9" stroke="#888" stroke-width="1.3"/></svg>
    </div>
  </nav>
  <section class="hero" role="img" aria-label="Photo of a hand using a tablet in an office">
    <div class="hero-arrow left"><svg width="8" height="10" viewBox="0 0 8 10"><path d="M6 1 2 5l4 4" fill="none" stroke="#444" stroke-width="1.6"/></svg></div>
    <div class="hero-arrow right"><svg width="8" height="10" viewBox="0 0 8 10"><path d="M2 1l4 4-4 4" fill="none" stroke="#444" stroke-width="1.6"/></svg></div>
    <div class="hero-caption">
      <p>Aenean mattis pharetra sapien, interdum ante congue id.</p>
      <span class="btn">Get Started Now</span>
    </div>
  </section>
  <div class="hero-rule"></div>
  <section class="features">
    <div class="feature"><div class="thumb kiosks" role="img" aria-label="Photo of rental kiosks at an event"></div><h3>Looking for <span>Kiosks?</span></h3></div>
    <div class="feature"><div class="thumb tablets" role="img" aria-label="Photo of a tablet on a stand"></div><h3>Looking for <span>Tablets?</span></h3></div>
    <div class="feature"><div class="thumb about" role="img" aria-label="Video about the company">
      <svg width="40" height="40" viewBox="0 0 40 40"><circle cx="20" cy="20" r="18" fill="none" stroke="#fff" stroke-width="2"/><path d="M16 12v16l12-8z" fill="#fff"/></svg>
    </div><h3>Know <span>About us</span></h3></div>
  </section>
  <div class="divider" style="margin-top:14px"></div>
  <section class="intro">
    <div class="intro-text">
      <h2>Etiam pulvinar bibendum eros</h2>
      <p>Mauris et quam volutpat, accumsan libero et, molestie risus. Duis ullamcorper nisi et sapien adipiscing adipiscing. Vivamus porta, tellus eget porttitor rhoncus, purus libero pellentesque nisl, sit amet placerat ipsum orci eu ipsum. Ut at orci vulputate, rutrum massa varius, suscipit augue. Etiam nec sollicitudin turpis. Cras et nibh ut urna vehicula aliquam. Ut vestibulum lacinia aliquet. Cras tincidunt elit consectetur dui tristique, et mollis sapien feugiat.</p>
      <p>Suspendisse pellentesque velit in lacinia iaculis. In at erat in enim commodo luctus id sed ante. Praesent ullamcorper tellus eget aliquet condimentum. Proin quam ligula, ullamcorper quis risus eget, ultricies dignissim libero. Duis volutpat lectus. Pellentesque porttitor porttitor aliquet.</p>
    </div>
    <div class="intro-photo" role="img" aria-label="Photo of a smiling woman holding a tablet"></div>
  </section>
  <div class="divider" style="margin-top:12px"></div>
  <section class="platforms" aria-label="Supported platforms">
    <div class="platform">Panelvue</div>
    <div class="platform">Slatehub</div>
    <div class="platform">Pivora</div>
  </section>
  <p class="tagline">Aenean posuere pharetra venenatis. Etiam tempus massa quam, eget congue eros accumsan quis. Mauris facilisis ipsum nec tincidunt, vitae tempus lectus aliquam. Pellentesque vitae nibh vel libero semper consectetur at nec tortor. Etiam varius suscipit semper.</p>
  <div class="divider" style="margin-top:20px"></div>
  <section class="partners" aria-label="Partners">
    <span></span><span></span><span></span><span></span><span></span><span></span><span></span><span></span><span></span>
  </section>
</div>
<footer>
  <div class="footer-info"><div class="wrap">
    <div class="item"><svg width="10" height="12" viewBox="0 0 10 12"><path d="M5 0a4 4 0 0 0-4 4c0 3 4 8 4 8s4-5 4-8a4 4 0 0 0-4-4z" fill="#999"/></svg>12, Harbor Lane, Westfield<br>City · 00-000</div>
    <div class="item"><svg width="10" height="10" viewBox="0 0 24 24"><path fill="#999" d="M6.6 10.8a15 15 0 0 0 6.6 6.6l2.2-2.2c.3-.3.7-.4 1-.2 1.1.4 2.3.6 3.6.6.6 0 1 .4 1 1V20c0 .6-.4 1-1 1A17 17 0 0 1 3 4c0-.6.4-1 1-1h3.5c.6 0 1 .4 1 1 0 1.3.2 2.5.6 3.6.1.3 0 .7-.2 1z"/></svg>Phone 555 014 2290</div>
    <div class="item"><svg width="10" height="10" viewBox="0 0 10 10"><rect x="1" y="2" width="8" height="6" fill="#999"/></svg>Fax : 555 014 2291</div>
    <div class="item"><svg width="12" height="9" viewBox="0 0 12 9"><rect width="12" height="9" fill="#999"/><path d="M0 0l6 5 6-5" fill="none" stroke="#ececec"/></svg>E-mail : hello@bolumexa.com</div>
  </div></div>
  <div class="footer-bar"><div class="wrap">
    <div class="footer-links"><a>Home</a>| <a>About</a>| <a>Services</a>| <a>Products</a>| <a>Pricing</a>| <a>Contact</a></div>
    <p>Copyright © 2014 · Bolumexa · All rights reserved.</p>
    <div class="social" aria-label="Social links"><i></i><i></i></div>
  </div></div>
</footer>
</body>
</html>
```